Flyer for language school

Hi,
We are language school, we offre german courses.
We will provide our students with a notepad during registration in a german course.
For that, we need the front page ofthe notepad to be pretty, simple and remarkable.
U can find our colors in the logo in the attachement.
for the contact information, we need those three adresses
Tunis - Imm Les Cyprès, 3ème étage 47 Rue des Mimosas, 2089 Les Jardins du Nord 3
Tél : 71 438 506
Email : tunis@lerbavo.org
Sfax - Imm Yasmina, 5ème étage Rue Karim Bensaid (en face de la rtpm), 3142 Sfax
Tél : 74 815 672
Email : sfax@lerbavo.org
Sousse - 14 Ave Hédi Marzouki (prés du rond point Horizon au dessus du café Mirabelle).
Tél : 73 592 031
Email : sousse@lerbavo.org
The website needs to be cited also :
www.lerbavo.org

```html
<!DOCTYPE html>
<html lang="fr">
<head>
<meta charset="utf-8">
<title>Lerbavo – Couverture de bloc-notes</title>
<link rel="stylesheet" href="https://fonts.googleapis.com/css2?family=Open+Sans:wght@700;800&display=swap">
<style>
  :root {
    --lime: #dde021;
    --stone: #bdbdbb;
    --charcoal: #4a4a45;
    --ink: #3b3b37;
    --paper: #ffffff;
  }
  * { margin: 0; padding: 0; box-sizing: border-box; }
  html, body {
    width: 849px;
    height: 1200px;
    overflow: hidden;
    background: var(--paper);
  }
  .cover {
    position: relative;
    width: 849px;
    height: 1200px;
    font-family: "Open Sans", Arial, sans-serif;
    color: var(--ink);
  }
  .hex-field {
    position: absolute;
    left: 0; top: 0;
    width: 849px;
    height: 1013px;
    background:
      radial-gradient(circle at 20% 25%, var(--stone) 0 14%, transparent 34%),
      radial-gradient(circle at 75% 55%, var(--lime) 0 12%, transparent 36%),
      radial-gradient(circle at 35% 80%, var(--stone) 0 10%, transparent 32%),
      linear-gradient(160deg, var(--charcoal) 0%, #7d7d64 35%, #b6b850 60%, var(--charcoal) 100%);
  }
  .brand-corner {
    position: absolute;
    right: 0; top: 0;
    width: 330px;
    height: 250px;
    background: var(--paper);
    clip-path: polygon(12% 0, 100% 0, 100% 80%, 72% 80%, 62% 100%, 34% 100%, 24% 80%, 30% 60%, 20% 40%, 0 40%);
  }
  .brand {
    position: absolute;
    right: 40px;
    top: 96px;
    display: flex;
    align-items: center;
    gap: 12px;
  }
  .brand-dot {
    width: 34px;
    height: 34px;
    border-radius: 50%;
    background: var(--lime);
  }
  .brand-name {
    font-size: 46px;
    font-weight: 800;
    letter-spacing: -1px;
    color: var(--charcoal);
  }
  .contact-band {
    position: absolute;
    left: 0; top: 1013px;
    width: 849px;
    height: 187px;
    background: var(--lime);
    padding: 26px 28px 0;
  }
  .website {
    font-size: 11px;
    font-weight: 700;
    margin-bottom: 16px;
  }
  .offices {
    display: grid;
    grid-template-columns: 269px 263px 1fr;
  }
  .office {
    font-size: 10.5px;
    font-weight: 700;
    line-height: 13px;
    padding-right: 18px;
  }
  .office p + p { margin-top: 0; }
</style>
</head>
<body>
<main class="cover">
  <div class="hex-field" role="img" aria-label="Motif de grands hexagones jaunes, gris clair et gris foncé en mosaïque"></div>

  <div class="brand-corner"></div>
  <div class="brand">
    <span class="brand-dot"></span>
    <span class="brand-name">lerbavo</span>
  </div>

  <footer class="contact-band">
    <p class="website">www.lerbavo.org</p>
    <div class="offices">
      <section class="office">
        <p>Tunis - Imm Les Cyprès, 3ème étage 47 Rue des Mimosas, 2089 Les Jardins du Nord 3</p>
        <p>Tél : 71 438 506</p>
        <p>Email : tunis@lerbavo.org</p>
      </section>
      <section class="office">
        <p>Sfax - Imm Yasmina, 5ème étage Rue Karim Bensaid (en face de la rtpm), 3142 Sfax</p>
        <p>Tél : 74 815 672</p>
        <p>Email : sfax@lerbavo.org</p>
      </section>
      <section class="office">
        <p>Sousse - 14 Ave Hédi Marzouki (prés du rond point Horizon au dessus du café Mirabelle).</p>
        <p>Tél : 73 592 031</p>
        <p>Email : sousse@lerbavo.org</p>
      </section>
    </div>
  </footer>
</main>
</body>
</html>
```